Property developer, money partner needs business card design using logo concept provided

Our company develops residential properties, does money lends for joint ventures in property deals and finds property deals for other money partners. We have provided a basic logo for you to work from. Any graphic or logo design on the card is to communicate development and finance collaboration. Color choice is not so important for us, but color choice does need to reflect professionalism.

```html
<!DOCTYPE html>
<html lang="en">
<head>
<meta charset="utf-8">
<title>Keystone Property Solutions – Business Card</title>
<link href="https://fonts.googleapis.com/css2?family=Open+Sans:wght@400;600;700&display=swap" rel="stylesheet">
<style>
  :root {
    --backdrop: #3b3b3b;
    --card: #151515;
    --card-edge: #1e78d2;
    --accent-blue: #1f74cc;
    --accent-red: #b3262c;
    --text-light: #ececec;
    --text-muted: #bdbdbd;
    --pattern-dark: #1c1c1c;
    --pattern-light: #333333;
  }
  * { margin: 0; padding: 0; box-sizing: border-box; }
  html, body {
    width: 1200px; height: 801px; overflow: hidden;
    background: var(--backdrop);
    font-family: "Open Sans", Arial, sans-serif;
  }
  .stage {
    position: relative; width: 1200px; height: 801px;
    display: flex; align-items: center; justify-content: center; gap: 50px;
  }
  .card {
    position: relative; width: 525px; height: 300px;
    background: var(--card);
    border-bottom: 3px solid var(--card-edge);
    border-left: 2px solid var(--card-edge);
    box-shadow: 0 14px 30px rgba(0,0,0,0.45);
    overflow: hidden;
  }
  /* Front */
  .card-front { display: flex; }
  .brand-panel {
    width: 50%; display: flex; flex-direction: column;
    align-items: center; justify-content: center; gap: 10px;
  }
  .brand-mark {
    display: flex; align-items: center; gap: 10px;
  }
  .brand-dot {
    width: 26px; height: 26px; border-radius: 50%;
    background: var(--accent-blue);
  }
  .brand-name {
    font-weight: 700; font-size: 26px; letter-spacing: 4px;
    color: var(--text-light);
  }
  .brand-tagline {
    font-size: 12px; letter-spacing: 2px; color: var(--text-muted);
  }
  .brand-reg {
    font-size: 7px; letter-spacing: 2px; color: var(--text-muted);
  }
  .divider {
    position: absolute; left: 50%; top: 118px; bottom: 40px;
    width: 1px; background: var(--accent-blue);
  }
  .contact-panel {
    width: 50%; padding: 44px 0 0 28px;
    color: var(--text-light);
  }
  .person-name {
    font-weight: 700; font-size: 21px; color: var(--accent-blue);
    letter-spacing: 0.5px;
  }
  .person-role { font-size: 13px; margin-bottom: 18px; }
  .address { font-size: 13px; line-height: 1.45; margin-bottom: 16px; }
  .contact-list { list-style: none; font-size: 13px; line-height: 1.7; }
  .contact-list li { display: flex; align-items: center; gap: 8px; }
  .contact-list svg { width: 11px; height: 11px; fill: var(--accent-red); flex: none; }
  /* Back */
  .card-back { display: flex; align-items: center; justify-content: center; }
  .pattern-field {
    position: absolute; inset: 0;
    background: linear-gradient(120deg, var(--pattern-dark) 0%, #262626 55%, var(--pattern-light) 100%);
  }
  .back-mark {
    position: relative; display: flex; align-items: center; gap: 10px;
    margin-left: 140px;
  }
  .back-mark .brand-name { font-size: 20px; letter-spacing: 3px; }
</style>
</head>
<body>
<main class="stage">
  <section class="card card-front" aria-label="Business card front">
    <div class="brand-panel">
      <div class="brand-mark">
        <span class="brand-dot"></span>
        <span class="brand-name">KEYSTONE</span>
      </div>
      <div class="brand-tagline">Property Solutions</div>
      <div class="brand-reg">A.C.N 123 456 789</div>
    </div>
    <span class="divider"></span>
    <div class="contact-panel">
      <h1 class="person-name">DAN WHITLOCK</h1>
      <p class="person-role">President</p>
      <p class="address">1820 Harbor Crest Dr<br>Bayview CA 90210</p>
      <ul class="contact-list">
        <li>
          <svg viewBox="0 0 24 24" aria-hidden="true"><path d="M6.6 10.8a15 15 0 0 0 6.6 6.6l2.2-2.2c.3-.3.7-.4 1-.2 1.1.4 2.3.6 3.6.6.6 0 1 .4 1 1V20c0 .6-.4 1-1 1A17 17 0 0 1 3 4c0-.6.4-1 1-1h3.5c.6 0 1 .4 1 1 0 1.3.2 2.5.6 3.6.1.3 0 .7-.2 1z"/></svg>
          555-010-4827
        </li>
        <li>
          <svg viewBox="0 0 24 24" aria-hidden="true"><path d="M2 5h20v14H2z M2 5l10 8 10-8" /></svg>
          dwhitlock@keystoneprop.com
        </li>
        <li>
          <svg viewBox="0 0 24 24" aria-hidden="true"><circle cx="12" cy="12" r="10"/></svg>
          www.keystoneprop.com
        </li>
      </ul>
    </div>
  </section>

  <section class="card card-back" aria-label="Business card back">
    <div class="pattern-field" role="img" aria-label="Repeating tone-on-tone pattern of the company symbol"></div>
    <div class="back-mark">
      <span class="brand-dot"></span>
      <span class="brand-name">KEYSTONE</span>
    </div>
  </section>
</main>
</body>
</html>
```